Pediatric Vision Care: Myopia Control Brochure

We are a pediatric eye care practice (ophthalmology and optometry). One of our services we offer for children is myopia control, which are strategies for slowing or stopping the progression of nearsightedness. This is a service we need to sell to parents because most insurance won't pay for it. There are different options we offer that can work well for kids in different situations: glasses with Corvane lenses, atropine eye drops, and/or special contact lenses. We need a brochure we can distribute to parents to let them know about this service that would encourage them to buy it for children who need it. Attached is our initial draft brochure created by our staff that provides text that we want to keep. The images and layout can change. We probably need at least one or two photos of kids on the brochure, because this is only something that works for children who are still growing, and the target audience is parents of 4-8 year old children.

Target Market(s)

Parents of 4-8 year old children

Font styles to use
Sans Serif

Requirements
Must have
• I'm uploading our company logo that should be included somewhere on the brochure. You can include contact information (web address, phone number) for our practice that is found on our website: http://www.brookhollowkidsvision.com/
Should not have
• This should not look childish. We need the impression to be friendly but professional, medical, expert.

```html
<!DOCTYPE html>
<html lang="en">
<head>
<meta charset="utf-8">
<title>Myopia Control for Children – Trifold Brochure</title>
<link rel="stylesheet" href="https://fonts.googleapis.com/css2?family=Outfit:wght@400;500;600;700;800&display=swap">
<style>
  :root{
    --navy:#243584;
    --gold:#e3b20c;
    --paper:#ececec;
    --ink:#2a2f45;
    --stage:#8a93b6;
    --photo-a:#5d6f86;
    --photo-b:#c9cdd6;
  }
  *{box-sizing:border-box;margin:0;padding:0}
  html,body{width:1200px;height:954px;overflow:hidden}
  body{background:var(--stage);font-family:"Outfit",sans-serif;color:var(--ink);position:relative}
  .spread{position:absolute;left:15px;width:1170px;height:440px;background:var(--paper);overflow:hidden;box-shadow:0 6px 18px rgba(20,30,70,.25)}
  .spread--outside{top:26px}
  .spread--inside{top:488px}
  .spread__art{position:absolute;inset:0;width:100%;height:100%}
  .fold{position:absolute;top:0;bottom:0;width:1px;background:rgba(0,0,0,.07)}
  .panel{position:absolute;top:0;height:440px;width:390px;padding:0 30px}
  .photo{position:absolute;border-radius:50%;border:4px solid var(--gold)}
  h2{font-weight:800;color:var(--navy);font-size:18px;line-height:1.15;margin-bottom:5px}
  h3{font-weight:700;color:var(--navy);font-size:11.5px;margin:7px 0 2px}
  p,li{font-size:10px;line-height:1.35}
  ul{list-style:none}
  li{position:relative;padding-left:11px}
  li::before{content:"";position:absolute;left:1px;top:5px;width:5px;height:5px;border-radius:50%;background:var(--gold)}
  strong{font-weight:700}
  .lead{font-weight:700;color:var(--navy);font-size:10px;margin-top:5px}
  .brand{display:flex;align-items:center;justify-content:center;gap:7px;font-weight:600;color:var(--navy);font-size:15px}
  .brand__dot{width:12px;height:12px;border-radius:50%;background:var(--gold)}
  .cover{text-align:center}
  .cover__title{font-weight:800;color:var(--navy);font-size:30px;line-height:1.02;margin-top:14px}
  .cover__title span{display:block;font-weight:500;font-size:27px}
  .cover__tagline{position:absolute;left:30px;right:30px;top:348px;color:#fff;text-align:center}
  .cover__tagline h4{font-weight:600;font-size:17px;line-height:1.15;margin-bottom:6px}
  .cover__tagline p{font-size:9.5px;font-style:italic}
  .contact{text-align:center;padding-top:66px}
  .contact h2{font-size:17px}
  .contact .cta{margin-top:10px}
  .contact .cta h3{font-size:12px;margin-top:3px}
  .contact-list{margin-top:9px;border-top:1px solid rgba(36,53,132,.15);padding-top:8px}
  .contact-item{margin-bottom:5px}
  .contact-item b{display:flex;align-items:center;justify-content:center;gap:4px;font-size:10.5px;color:var(--navy);font-weight:700}
  .contact-item span{font-size:10px;line-height:1.35;display:block}
  .site{position:absolute;left:390px;width:390px;top:412px;text-align:center;color:#fff;font-weight:700;font-size:13px;display:flex;align-items:center;justify-content:center;gap:6px}
  .subtle{color:var(--gold);font-style:italic;font-size:9.5px;margin-bottom:2px}
</style>
</head>
<body>

<section class="spread spread--outside" aria-label="Brochure outside">
  <svg class="spread__art" viewBox="0 0 1170 440" preserveAspectRatio="none" aria-hidden="true">
    <path d="M0,0 L780,0 L780,40 C560,54 300,38 0,18 Z" fill="var(--gold)"/>
    <path d="M0,18 C300,38 560,54 780,40 L780,46 C560,60 300,44 0,24 Z" fill="var(--navy)"/>
    <path d="M0,345 C200,385 450,405 650,400 C850,390 1000,288 1170,200 L1170,440 L0,440 Z" fill="var(--gold)"/>
    <path d="M0,355 C200,395 450,415 650,410 C850,400 1000,300 1170,212 L1170,440 L0,440 Z" fill="var(--navy)"/>
  </svg>
  <div class="fold" style="left:390px"></div>
  <div class="fold" style="left:780px"></div>

  <div class="panel" style="left:0;padding-top:62px">
    <h2>Environmental &amp; Lifestyle Support</h2>
    <p>All children with myopia benefit from healthy visual habits.</p>
    <h3>Outdoor Time</h3>
    <p>Children who spend at least <strong>2 hours outdoors daily</strong> are less likely to develop myopia, and may experience slower progression.</p>
    <p>Even an extra <strong>45 minutes per day outdoors</strong> can be beneficial.</p>
    <h3>Screen &amp; Near Work Habits</h3>
    <p>Excessive screen use, especially at close distance, may contribute to worsening myopia.</p>
    <p class="lead">We recommend:</p>
    <ul>
      <li>Limiting non-academic screen time</li>
      <li>Encouraging breaks during near work</li>
      <li>Using the 20-20-20 rule: Every 20 minutes, look 20 feet away for 20 seconds</li>
    </ul>
  </div>
  <div class="photo" role="img" aria-label="Photo of an eye drop falling from a dropper bottle" style="left:40px;top:326px;width:104px;height:104px;background:radial-gradient(circle at 40% 35%,#dfe6ec,#3b4a5a 70%)"></div>

  <div class="panel contact" style="left:390px">
    <h2>Environmental<br>and Lifestyle Support</h2>
    <p>Early care today can help protect your child's vision for the future. Myopia control is most effective when started early, while your child's eyes are still developing.</p>
    <p><strong>Give your child the advantage of clearer vision and reduced risk of eye problems later in life.</strong></p>
    <div class="cta">
      <svg width="20" height="20" viewBox="0 0 24 24" aria-hidden="true"><rect x="3" y="5" width="18" height="16" rx="2" fill="none" stroke="var(--navy)" stroke-width="2"/><path d="M3 10h18M8 3v4M16 3v4" stroke="var(--navy)" stroke-width="2"/><path d="M7 13h2M11 13h2M15 13h2M7 17h2M11 17h2" stroke="var(--gold)" stroke-width="2"/></svg>
      <h3>Schedule a Consultation Today</h3>
      <p>Our experienced pediatric eye care team will guide you through the best options tailored to your child's needs.</p>
    </div>
    <div class="contact-list">
      <div class="contact-item"><b><svg width="10" height="10" viewBox="0 0 24 24"><path d="M6 2l4 4-2 3c1 3 4 6 7 7l3-2 4 4-3 4C10 22 2 14 2 5z" fill="var(--gold)"/></svg>Call Us</b><span>(555) 214-0370</span></div>
      <div class="contact-item"><b><svg width="10" height="10" viewBox="0 0 24 24"><rect x="2" y="5" width="20" height="14" rx="2" fill="var(--gold)"/><path d="M2 6l10 7 10-7" stroke="#fff" stroke-width="2" fill="none"/></svg>Email Address</b><span>hello@brookhollowkidsvision.com</span></div>
      <div class="contact-item"><b><svg width="10" height="10" viewBox="0 0 24 24"><path d="M12 2a7 7 0 0 0-7 7c0 5 7 13 7 13s7-8 7-13a7 7 0 0 0-7-7z" fill="var(--gold)"/><circle cx="12" cy="9" r="2.5" fill="#fff"/></svg>Location</b><span>Brookhollow Kids Vision, 218 Alder Crest Road<br>Maple Hollow, VA 23019</span></div>
    </div>
  </div>
  <div class="site"><svg width="12" height="12" viewBox="0 0 24 24"><circle cx="12" cy="12" r="10" fill="var(--gold)"/><path d="M2 12h20M12 2c3 3 3 17 0 20M12 2c-3 3-3 17 0 20" stroke="var(--navy)" stroke-width="1.5" fill="none"/></svg>www.brookhollowkidsvision.com</div>

  <div class="panel cover" style="left:780px;padding-top:26px">
    <div class="brand"><span class="brand__dot"></span>Brookhollow Kids Vision</div>
    <div class="cover__title">Myopia Control<span>for Children</span></div>
    <div class="photo" role="img" aria-label="Photo of a smiling young girl wearing glasses and a school uniform" style="left:100px;top:132px;width:190px;height:190px;background:linear-gradient(160deg,var(--photo-a),var(--photo-b))"></div>
    <div class="cover__tagline">
      <h4>Slowing the Progression of Nearsightedness</h4>
      <p>Myopia (nearsightedness) is becoming increasingly common in children. Early management can help protect long-term vision health.</p>
    </div>
  </div>
</section>

<section class="spread spread--inside" aria-label="Brochure inside">
  <svg class="spread__art" viewBox="0 0 1170 440" preserveAspectRatio="none" aria-hidden="true">
    <path d="M0,0 L1170,0 L1170,62 C1000,54 880,40 760,50 C620,60 470,66 390,70 C250,74 120,92 0,116 Z" fill="var(--gold)"/>
    <path d="M0,0 L1170,0 L1170,52 C1000,44 880,30 760,40 C620,50 470,56 390,60 C250,64 120,82 0,106 Z" fill="var(--navy)"/>
    <path d="M390,398 C560,406 700,416 840,412 C960,409 1080,406 1170,402 L1170,440 L390,440 Z" fill="var(--gold)"/>
    <path d="M390,408 C560,416 700,426 840,422 C960,419 1080,416 1170,412 L1170,440 L390,440 Z" fill="var(--navy)"/>
  </svg>
  <div class="fold" style="left:390px"></div>
  <div class="fold" style="left:780px"></div>

  <div class="photo" role="img" aria-label="Photo of a young girl looking into an eye examination instrument" style="left:150px;top:12px;width:176px;height:176px;background:linear-gradient(135deg,#e4e6ea,#8b919b)"></div>
  <div class="panel" style="left:0;padding-top:206px">
    <h2>What is Myopia?</h2>
    <p>Myopia (nearsightedness) is a common vision condition in children that makes distant objects appear blurry. It occurs when the eye grows too long during childhood development, causing light to focus incorrectly inside the eye.</p>
    <p style="margin-top:5px">As children continue to grow, myopia often progresses over time, leading to stronger glasses prescriptions.</p>
    <h2 style="font-size:15px;margin-top:8px">Why Does It Matter?</h2>
    <p>Higher levels of myopia are linked to an increased risk of serious eye conditions later in life, including:</p>
    <ul>
      <li>Retinal complications</li>
      <li><strong>Macular degeneration</strong></li>
      <li>Other long-term vision problems</li>
    </ul>
  </div>

  <div class="panel" style="left:390px;padding-top:82px">
    <h2>What is Myopia Control?</h2>
    <p><strong>Myopia control</strong> includes specialized treatments designed to <strong>slow the progression of nearsightedness in children.</strong> Rather than simply correcting vision with glasses, these treatments help manage how the eye grows over time.</p>
    <h3>The Goals of Myopia Control</h3>
    <ul>
      <li>Slow the growth of the eye</li>
      <li>Keep glasses prescriptions lower over time</li>
      <li>Reduce the risk of future eye disease</li>
    </ul>
    <h3>Screen &amp; Near Work Habits</h3>
    <p>Excessive screen use, especially at close distance, may contribute to worsening myopia.</p>
    <p class="lead">We recommend:</p>
    <ul>
      <li>Limiting non-academic screen time</li>
      <li>Encouraging breaks during near work</li>
      <li>Using the 20-20-20 rule: Every 20 minutes, look 20 feet away for 20 seconds</li>
    </ul>
  </div>
  <div class="photo" role="img" aria-label="Photo of a soft contact lens resting on a fingertip" style="left:548px;top:362px;width:74px;height:74px;background:radial-gradient(circle at 50% 70%,#c46c6a,#2a1c1c 75%)"></div>

  <div class="panel" style="left:780px;padding-top:68px">
    <h2>Treatment Options</h2>
    <p class="subtle">We offer several proven myopia control options:</p>
    <h3>Halvern Corvane Glasses</h3>
    <p>FDA market-authorized lenses shown to slow myopia progression by approximately 50% in children ages 6–12.</p>
    <ul>
      <li>Look like regular glasses</li>
      <li>Special lens design helps signal the eye to slow growth</li>
      <li>Easy daily use</li>
    </ul>
    <h3>Low-Dose Atropine Eye Drops</h3>
    <p>Clinically studied for over 20 years and shown to reduce progression by about 50%.</p>
    <ul>
      <li>One drop in each eye at bedtime</li>
      <li>Simple daily routine</li>
      <li>Prepared by a compounding pharmacy and delivered to your home</li>
    </ul>
    <h3>Specialty Contact Lenses (ClaraView)</h3>
    <p>FDA-approved lenses shown to slow progression by about 50% in children ages 8–12.</p>
    <ul>
      <li>Great for active children</li>
      <li>Alternative to glasses</li>
      <li>Many children adapt successfully as young as 7–8 years old</li>
    </ul>
  </div>
</section>

</body>
</html>
```